Alberta, Canada based Environmental Oilfield Consultant need a Business Card Design

We need a business card design for a year old company based in Cedarvale, Ridgeway, Canada called Brambleton Consulting Inc. We are environmental consultants primarily for oilfield based companies (pipeline cleanup, site consultations, environmental site training, and site evaluations).

We like the color blue or green, something very clean and crisp looking.
We don't really care if there is an otter on it but most of our work is land based and nothing really to do with oceans or larger bodies of water.

The name Brambleton was the name of our fathers boat, and named our company that in his memory.

```html
<!DOCTYPE html>
<html lang="en">
<head>
<meta charset="utf-8">
<title>Brambleton Consulting Inc. – Business Card</title>
<link rel="stylesheet" href="https://fonts.googleapis.com/css2?family=Questrial&family=Montserrat:wght@600&display=swap">
<style>
  :root {
    --page-bg: #e9ecef;
    --card-bg: #ffffff;
    --brand-blue: #1272b8;
    --brand-green: #2bb673;
    --shadow: rgba(0, 0, 0, 0.28);
  }
  html, body {
    margin: 0;
    width: 1200px;
    height: 900px;
    overflow: hidden;
    background: var(--page-bg);
  }
  .business-card {
    position: absolute;
    left: 150px;
    top: 193px;
    width: 900px;
    height: 514px;
    background: var(--card-bg);
    box-shadow: 0 10px 28px var(--shadow);
    overflow: hidden;
    font-family: "Questrial", sans-serif;
  }
  .corner-accent {
    position: absolute;
    inset: 0;
    width: 100%;
    height: 100%;
  }
  .brand-mark {
    position: absolute;
    left: 26px;
    top: 40px;
    width: 78px;
    height: 78px;
    border-radius: 50%;
    background: var(--brand-green);
  }
  .company-name {
    position: absolute;
    left: 24px;
    top: 128px;
    margin: 0;
    font-weight: 400;
    font-size: 44px;
    letter-spacing: 0.5px;
    color: var(--brand-blue);
    white-space: nowrap;
  }
  .contact-block {
    position: absolute;
    left: 30px;
    top: 262px;
  }
  .person-name {
    margin: 0;
    font-family: "Montserrat", sans-serif;
    font-weight: 600;
    font-size: 30px;
    color: var(--brand-blue);
  }
  .person-title {
    margin: 2px 0 26px;
    font-size: 24px;
    color: var(--brand-green);
  }
  .contact-line {
    margin: 0 0 6px;
    font-size: 25px;
    color: var(--brand-green);
    letter-spacing: 0.5px;
    white-space: nowrap;
  }
  .contact-label {
    font-family: "Montserrat", sans-serif;
    font-weight: 600;
    color: var(--brand-blue);
    letter-spacing: 0;
  }
  .contact-gap {
    display: inline-block;
    width: 34px;
  }
</style>
</head>
<body>
  <div class="business-card">
    <svg class="corner-accent" viewBox="0 0 900 514" preserveAspectRatio="none" aria-hidden="true">
      <path class="accent-green" fill="var(--brand-green)"
        d="M 900 230 Q 760 450 470 514 L 540 514 Q 790 465 900 280 Z"/>
      <path class="accent-blue" fill="var(--brand-blue)"
        d="M 900 300 Q 800 470 580 514 L 900 514 Z"/>
    </svg>

    <div class="brand-mark"></div>
    <h1 class="company-name">Brambleton Consulting Inc.</h1>

    <div class="contact-block">
      <p class="person-name">Name</p>
      <p class="person-title">Designation</p>
      <p class="contact-line"><span class="contact-label">ph:</span> 1234567890<span class="contact-gap"></span><span class="contact-label">fax:</span> 1234567890</p>
      <p class="contact-line"><span class="contact-label">e-mail:</span> name@brambletoninc.com</p>
      <p class="contact-line"><span class="contact-label">add.:</span> Cedarvale, Ridgeway, Canada</p>
    </div>
  </div>
</body>
</html>
```